Tomas's Business Cards

My husband is a self employed Cabinet Maker... who contracts to Building companies and clients directly.
He installs kitchesn, designs and also completes renovations and building work.

I would like a small, FUNKY, simple but eye catching design.

It needs to incorporate the following.
Custom Cabinets / Installations / Renovations / Design

Commercial and Residential

He does not have a Website or Chatterly,
contact number is 0438 207 619 and email is tomasvelkin@quillmail.example

I would like a Grey/Silver on black, or blue covering.. I am open to colour designs?

Thank you. :-)

Target Market(s)

Building Companies
Clients
Other Trades people onsite,. to give out at job sites

Industry/Entity Type

Business

Contact Information for Business Card

Phone: 0438 207 619
Email: tomasvelkin@quillmail.example

Font styles to use
Sans Serif

Colors
0592cd
747474
474747
1b1b1b
85cae6

Requirements
Must have
• Funky, simple, eye catching design
• Would like use of Silver/Grey - and a colour that would complement this.
• Am open to ideas :-)
Nice to have
• We do not have a logo or picture, will leave this up to you if you think an image would be beneficial???
• Thank you.

```html
<!DOCTYPE html>
<html lang="en">
<head>
<meta charset="utf-8">
<title>Tomas Velkin – Business Card</title>
<link rel="stylesheet" href="https://fonts.googleapis.com/css2?family=Exo+2:wght@300;400&family=Michroma&display=swap">
<style>
  :root {
    --page-bg: #f4f4f4;
    --card-black: #1b1b1b;
    --card-deep: #0c0c0c;
    --card-glow: #2a2a2a;
    --silver-light: #e6e6e6;
    --silver-mid: #b4b4b4;
    --silver-dark: #747474;
    --ink-dark: #1b1b1b;
    --brand-blue: #2f4fc4;
    --email-grey: #9a9a9a;
  }
  html, body {
    margin: 0;
    padding: 0;
    width: 1200px;
    height: 900px;
    overflow: hidden;
    background: var(--page-bg);
  }
  .card {
    position: absolute;
    left: 150px;
    top: 190px;
    width: 900px;
    height: 520px;
    border-radius: 36px;
    background: radial-gradient(ellipse at 50% 48%, var(--card-glow) 0%, var(--card-black) 45%, var(--card-deep) 100%);
    box-shadow: 0 14px 30px rgba(0,0,0,0.18);
    overflow: hidden;
  }
  .brand-mark {
    position: absolute;
    top: 62px;
    left: 0;
    width: 100%;
    display: flex;
    justify-content: center;
    align-items: center;
    gap: 16px;
  }
  .brand-mark__square {
    width: 30px;
    height: 30px;
    background: var(--brand-blue);
  }
  .brand-mark__name {
    font-family: "Exo 2", sans-serif;
    font-weight: 400;
    font-size: 54px;
    color: var(--brand-blue);
    letter-spacing: 2px;
  }
  .owner-name {
    position: absolute;
    top: 160px;
    width: 100%;
    text-align: center;
    font-family: "Exo 2", sans-serif;
    font-weight: 300;
    font-size: 62px;
    color: var(--silver-light);
    letter-spacing: 1px;
    margin: 0;
  }
  .services-band {
    position: absolute;
    top: 262px;
    left: 0;
    width: 100%;
    height: 36px;
    background: linear-gradient(180deg, var(--silver-light) 0%, var(--silver-mid) 55%, var(--silver-dark) 100%);
    display: flex;
    justify-content: center;
    align-items: center;
    font-family: "Michroma", sans-serif;
    font-size: 17px;
    color: var(--ink-dark);
    letter-spacing: 1.5px;
    white-space: nowrap;
  }
  .market-line {
    position: absolute;
    top: 322px;
    width: 100%;
    text-align: center;
    font-family: "Michroma", sans-serif;
    font-size: 16px;
    color: var(--brand-blue);
    letter-spacing: 20px;
    white-space: nowrap;
  }
  .contact {
    position: absolute;
    top: 385px;
    width: 100%;
    text-align: center;
    font-family: "Exo 2", sans-serif;
  }
  .contact__phone {
    display: block;
    font-size: 42px;
    font-weight: 400;
    color: var(--brand-blue);
    letter-spacing: 1px;
  }
  .contact__email {
    display: block;
    margin-top: 2px;
    font-size: 28px;
    font-weight: 400;
    color: var(--email-grey);
  }
</style>
</head>
<body>
  <div class="card">
    <div class="brand-mark">
      <span class="brand-mark__square"></span>
      <span class="brand-mark__name">Velkin</span>
    </div>
    <h1 class="owner-name">Tomas Velkin</h1>
    <div class="services-band">CUSTOM CABINETS / INSTALLATIONS / RENOVATIONS / DESIGN</div>
    <div class="market-line">COMMERCIAL AND RESIDENTIAL</div>
    <div class="contact">
      <span class="contact__phone">0438 207 619</span>
      <span class="contact__email">tomasvelkin@quillmail.example</span>
    </div>
  </div>
</body>
</html>
```